Shelter is Kinship Care Fact Sheet (2 sided page)

We are looking to create a 2-page Fact Sheet (front and back)
- The head logo is going to be: Shelter is Kinship Care
- The title of the fact sheet will be: Get the Facts on Mpox Vaccination
- Please include QB7's logo - please make sure there is room for another logo next to this (this is not included at this time)
- Use the colors and font and mimic the feel of our past resources from qbsevenfold.org/resources
- The main image should be incorporated for design (this is the beading circle image with 3 people beading) - additional images (feather & braided sweetgrass) can be included as needed for elements
- Do not put text over graphics and keep it simple and easy to read with high contrast.
- We want some very simple design element(s) incorporated that convey Native American communities or heritage. But NO headdress, teepee graphics, etc.
- Ensure that linked text remains in document for virtual use
- Please include this list before the funding statement - For more information, please visit:
www.qbsevenfold.org/vaccines
www.moreabove.org/campaigns/mpox/
www.hwb.example/poxvirus/mpox/
- Please remember to include the funding statement - it can be in a very small font 6/7 point. "This project: Bridging Regional Networks to Strengthen Neighborhood-Led Groups to Expand Immunization Reach Among Varied Cultural and Heritage Adult Groups Presently Facing Gaps is supported by the Bureau for Wellness and Outbreak Readiness (BWO) of the U.S. Office of Wellbeing and Civic Care (OWC) as part of a financial assistance award totaling $5,000,000 with 100 percent funded by BWO/OWC. The contents are those of the author(s) and do not necessarily represent the official views of, nor an endorsement by, BWO/OWC or the U.S. Government. "

Target Market(s)

American Indian and Alaska Native Two Spirit Indigiqueer

Requirements
Must have
• Global Alliance for Elder Kinfolk Wellness (QB7) color scheme - see website

```html
<!DOCTYPE html>
<html lang="en">
<head>
<meta charset="utf-8">
<title>Get the Facts on Mpox Vaccination – Back</title>
<link rel="stylesheet" href="https://fonts.googleapis.com/css2?family=Poppins:ital,wght@0,400;0,600;0,700;1,400&display=swap">
<style>
  :root {
    --teal: #468a89;
    --teal-button: #4a9195;
    --maroon: #7a1426;
    --button-edge: #b0404a;
    --fact-brown: #6b3410;
    --cream: #efe6d6;
    --blush: #f3cdbf;
    --white: #ffffff;
    --footer-text: #e3eeee;
  }
  * { margin: 0; padding: 0; box-sizing: border-box; }
  html, body { width: 797px; height: 1200px; overflow: hidden; }
  body { font-family: "Poppins", sans-serif; background: var(--teal); }
  .sheet { position: relative; width: 797px; height: 1200px; overflow: hidden; }

  .facts-panel { position: absolute; left: 0; top: 0; width: 797px; height: 701px; background: var(--teal); }
  .panel-texture {
    position: absolute; right: 0; top: 0; width: 110px; height: 701px;
    background: linear-gradient(90deg, rgba(255,255,255,0) 0%, rgba(255,255,255,0.05) 100%);
  }
  .point {
    position: absolute; left: 43px; display: flex; align-items: center;
    color: var(--white); font-weight: 600; font-size: 17.6px; line-height: 21px;
  }
  .diamond {
    flex: none; width: 13px; height: 13px; margin-right: 21px; margin-left: 6px;
    background: var(--maroon); transform: rotate(45deg);
  }
  .fact-note {
    position: absolute; left: 78px; color: var(--fact-brown);
    font-style: italic; font-size: 12px; line-height: 16px;
  }
  .side-effects {
    position: absolute; left: 76px; top: 349px; list-style: none;
    color: var(--white); font-weight: 600; font-size: 14.4px; line-height: 22px;
  }
  .side-effects li::before { content: "•"; color: #d0303c; margin-right: 5px; }

  .chevron-band {
    position: absolute; left: 0; top: 701px; width: 797px; height: 42px;
    background: linear-gradient(180deg, var(--cream) 0%, #2f7f85 35%, #5a4f60 65%, #8a2a3a 100%);
  }

  .links-panel { position: absolute; left: 0; top: 743px; width: 797px; height: 298px; background: var(--cream); }
  .links-texture {
    position: absolute; right: 0; top: 0; width: 177px; height: 298px;
    background: linear-gradient(90deg, rgba(243,205,191,0) 0%, var(--blush) 60%, rgba(243,205,191,0.7) 100%);
    opacity: 0.75;
  }
  .links-heading {
    position: absolute; top: 52px; left: 0; width: 786px; text-align: center;
    color: var(--fact-brown); font-weight: 700; font-size: 15.5px;
  }
  .link-button {
    position: absolute; left: 117px; width: 528px; height: 41px;
    display: flex; align-items: center; justify-content: center;
    background: var(--teal-button);
    border-left: 3px solid var(--button-edge); border-right: 3px solid var(--button-edge);
    color: var(--white); font-weight: 600; font-size: 22px; text-decoration: none; white-space: nowrap;
  }

  .funding { position: absolute; left: 0; top: 1041px; width: 797px; height: 159px; background: var(--teal); }
  .funding p {
    position: absolute; left: 32px; top: 22px; width: 750px;
    color: var(--footer-text); font-size: 11.6px; line-height: 17px;
  }
</style>
</head>
<body>
<main class="sheet">
  <section class="facts-panel">
    <div class="panel-texture" role="img" aria-label="Faint beadwork-inspired background pattern"></div>

    <div class="point" style="top:39px"><span class="diamond"></span><span>Get vaccinated as soon as possible after being exposed<br>to someone with mpox (if exposed less than 14 days ago,<br>ideally within 4 days of exposure).</span></div>
    <p class="fact-note" style="top:106px">Fact: You can call the shots.</p>

    <div class="point" style="top:129px"><span class="diamond"></span><span>Reduce scarring by asking about how and where to get the<br>mpox vaccine on your body, such as on the back of your upper arm.</span></div>

    <div class="point" style="top:189px"><span class="diamond"></span><span>Fact: Not everyone has side effects, but some people do.</span></div>
    <div class="point" style="top:232px"><span class="diamond"></span><span>Fact: Not everyone has side effects, but some people do.</span></div>
    <div class="point" style="top:271px"><span class="diamond"></span><span>The most common side effects after the VANTREX vaccine are:</span></div>
    <div class="point" style="top:315px"><span class="diamond"></span><span>The most common side effects after the VANTREX vaccine are:</span></div>

    <ul class="side-effects">
      <li>Pain, redness, and itching at the spot the vaccine is given</li>
      <li>Fever, headache, tiredness, nausea, chills, and muscle aches</li>
    </ul>

    <div class="point" style="top:406px"><span class="diamond"></span><span>These area signs that your immune system is responding,<br>not that you are getting sick.</span></div>
    <p class="fact-note" style="top:462px">Fact: Mpox vaccines are free.</p>

    <div class="point" style="top:489px"><span class="diamond"></span><span>Providers must give you the vaccine regardless of your ability<br>to pay the administration fee. Learn more and find an<br>mpox vaccine site near you.</span></div>
    <p class="fact-note" style="top:558px">Fact: Mpox vaccines are safe and effective.</p>

    <div class="point" style="top:579px"><span class="diamond"></span><span>Over one million vaccine doses have been given in the US with no<br>new or unexpected safety concerns and serious adverse events<br>to the mpox vaccine are rare. People who have been vaccinated<br>can still get mpox, but vaccination may make illness less severe.</span></div>
  </section>

  <div class="chevron-band" role="img" aria-label="Chevron border in teal and maroon"></div>

  <section class="links-panel">
    <div class="links-texture" role="img" aria-label="Soft pink geometric beadwork pattern"></div>
    <h2 class="links-heading">For more information, please visit:</h2>
    <a class="link-button" style="top:83px" href="https://www.qbsevenfold.org/vaccines">www.qbsevenfold.org/vaccines</a>
    <a class="link-button" style="top:146px" href="https://www.moreabove.org/campaigns/mpox/">www.moreabove.org/campaigns/mpox/</a>
    <a class="link-button" style="top:208px" href="https://www.hwb.example/poxvirus/mpox/">www.hwb.example/poxvirus/mpox/</a>
  </section>

  <footer class="funding">
    <p>This project: Bridging Regional Networks to Strengthen Neighborhood-Led Groups to Expand Immunization Reach Among Varied Cultural and Heritage Adult Groups Presently Facing Gaps is supported by the Bureau for Wellness and Outbreak Readiness (BWO) of the U.S. Office of Wellbeing and Civic Care (OWC) as part of a financial assistance award totaling $5,000,000 with 100 percent funded by BWO/OWC. The contents are those of the author(s) and do not necessarily represent the official views of, nor an endorsement by, BWO/OWC or the U.S. Government.</p>
  </footer>
</main>
</body>
</html>
```